Baby Sling

We need packaging designed for our new baby sling. We need it to project a premium product that is high quality, eco-friendly and appeals to Mums and Dads. It must be gender neutral, yet incorporate some of our logo colours of pink and green. Perhaps it could include some neutral colours such as light brown/mocha/latte.
We are happy if the images are 3D rendered.
The essence of our brand is high quality, eco-friendly, natural baby products and we would like this reflected in our packaging design.
Additionally, we need our logo fixed. The wording around the centre image is slightly off and needs to be balanced, should be very easy to do.
Updates

Reason: To allow designers more time to submit

Target Market(s)

Mums and Dads with new baby

Industry/Entity Type

Baby

Requirements
Must have
• Our logo, images of sling, features and benefits

```html
<!DOCTYPE html>
<html lang="en">
<head>
<meta charset="utf-8">
<title>Adjustable Baby Sling – Packaging Front Panel</title>
<link href="https://fonts.googleapis.com/css2?family=Archivo+Black&family=Oswald:wght@600;700&family=Roboto+Condensed:ital,wght@0,700;1,700&display=swap" rel="stylesheet">
<style>
  :root {
    --stage: #e9e9ea;
    --gold-light: #f4dfa6;
    --gold: #c9a45a;
    --gold-deep: #8a6a2c;
    --brown: #3a2712;
    --brown-dark: #1e1308;
    --cream: #f6ecd2;
    --teal: #3fc7c4;
    --pink: #e0457b;
    --ink: #111;
    --white: #fff;
  }
  * { margin: 0; padding: 0; box-sizing: border-box; }
  html, body { width: 1200px; height: 1200px; overflow: hidden; background: var(--stage); }
  .box-front {
    position: absolute; left: 220px; top: 40px; width: 760px; height: 1120px;
    overflow: hidden;
    background: linear-gradient(125deg, var(--gold) 0%, var(--gold-light) 30%, var(--gold) 55%, var(--brown) 85%, var(--brown-dark) 100%);
  }
  .box-front svg.art { position: absolute; inset: 0; }
  .badge {
    position: absolute; border-radius: 50%; border: 4px solid var(--ink);
    display: flex; flex-direction: column; align-items: center; justify-content: center;
    font-family: "Roboto Condensed", sans-serif; font-weight: 700; color: var(--ink);
    text-align: center; line-height: 1.1; background: rgba(255,255,255,0.08);
  }
  .badge::after {
    content: ""; position: absolute; inset: 5px; border-radius: 50%; border: 2px solid var(--ink);
  }
  .badge--quality { left: 204px; top: 88px; width: 124px; height: 124px; font-size: 16px; }
  .badge--quality .badge__lead { font-size: 18px; }
  .badge--cotton { left: 83px; top: 208px; width: 124px; height: 124px; font-size: 17px; }
  .badge--cotton .badge__big { font-size: 24px; }
  .badge--cotton .badge__gap { height: 22px; }
  .badge--weight { left: 76px; top: 392px; width: 138px; height: 138px; font-size: 22px; }
  .badge--weight .badge__big { font-family: "Archivo Black", sans-serif; font-size: 42px; line-height: 1; }
  .badge--weight .badge__big small { font-size: 17px; }
  .new-flag {
    position: absolute; left: 8px; top: 62px; transform: rotate(-45deg);
    font-family: "Archivo Black", sans-serif; font-size: 44px; color: var(--ink);
    letter-spacing: 1px;
  }
  .title { position: absolute; left: 150px; top: 735px; }
  .title__small {
    font-family: "Oswald", sans-serif; font-weight: 700; font-size: 44px; color: var(--white);
    text-shadow: 2px 2px 0 var(--ink), -1px -1px 0 var(--ink), 1px -1px 0 var(--ink), -1px 1px 0 var(--ink);
    line-height: 1;
  }
  .title__main {
    font-family: "Archivo Black", sans-serif; font-size: 96px; line-height: 1.05;
    letter-spacing: -2px; margin-left: 4px;
    color: #e9c86a;
    text-shadow: 3px 3px 0 var(--ink), -2px -2px 0 var(--ink), 2px -2px 0 var(--ink), -2px 2px 0 var(--ink), 5px 6px 6px rgba(0,0,0,0.5);
  }
  .tagline {
    position: absolute; left: 178px; right: 14px; top: 1052px;
    font-family: "Roboto Condensed", sans-serif; font-style: italic; font-weight: 700;
    font-size: 12px; line-height: 16px; color: var(--cream); white-space: nowrap; text-align: right;
  }
  .brand {
    position: absolute; left: 24px; top: 962px; width: 140px; height: 140px; border-radius: 50%;
    background: var(--brown-dark); border: 5px solid var(--gold);
    display: flex; align-items: center; justify-content: center; text-align: center;
    font-family: "Oswald", sans-serif; font-weight: 600; font-size: 26px; line-height: 1.1; color: var(--pink);
  }
</style>
</head>
<body>
  <main class="box-front">
    <svg class="art" width="760" height="1120" viewBox="0 0 760 1120">
      <defs>
        <radialGradient id="eggGlow" cx="55%" cy="40%" r="65%">
          <stop offset="0%" stop-color="#fbf1d4"/>
          <stop offset="55%" stop-color="#e4c27a"/>
          <stop offset="100%" stop-color="#9a7433"/>
        </radialGradient>
        <radialGradient id="photoTone" cx="50%" cy="45%" r="60%">
          <stop offset="0%" stop-color="#f1dcc2"/>
          <stop offset="45%" stop-color="#4fbfbc"/>
          <stop offset="100%" stop-color="#1c1410"/>
        </radialGradient>
        <linearGradient id="ringGold" x1="0" y1="0" x2="1" y2="1">
          <stop offset="0%" stop-color="#fff0b8"/>
          <stop offset="50%" stop-color="#c9a045"/>
          <stop offset="100%" stop-color="#6d4f1c"/>
        </linearGradient>
      </defs>
      <ellipse class="egg-glow" cx="500" cy="530" rx="260" ry="470" fill="url(#eggGlow)"/>
      <ellipse class="egg-ring" cx="500" cy="530" rx="260" ry="470" fill="none" stroke="url(#ringGold)" stroke-width="8"/>
      <ellipse class="egg-ring-outer" cx="500" cy="530" rx="270" ry="480" fill="none" stroke="#2a1b0b" stroke-width="8"/>
      <ellipse class="product-photo" role="img" aria-label="Photo of a smiling mother carrying her baby in a turquoise cotton sling"
        cx="505" cy="520" rx="225" ry="430" fill="url(#photoTone)"/>
      <polygon class="new-corner" points="0,0 230,0 0,230" fill="#f1d98a"/>
      <polygon class="new-corner-edge" points="0,190 190,0 230,0 0,230" fill="#2a1b0b"/>
      <rect class="info-band" x="0" y="1030" width="760" height="60" fill="#1e1308"/>
      <rect class="info-band-line" x="0" y="1026" width="760" height="4" fill="#c9a45a"/>
      <rect class="base-strip" x="0" y="1090" width="760" height="30" fill="#c9a45a"/>
    </svg>

    <div class="new-flag">NEW</div>

    <div class="badge badge--quality">
      <span class="badge__lead">Premium</span>
      <span>HIGHT</span>
      <span>QUALITY</span>
    </div>
    <div class="badge badge--cotton">
      <span class="badge__big">100%</span>
      <span class="badge__gap"></span>
      <span>COTTON</span>
    </div>
    <div class="badge badge--weight">
      <span>Birth to</span>
      <span class="badge__big">16<small> kg.</small></span>
    </div>

    <div class="title">
      <div class="title__small">Adjustable</div>
      <div class="title__main">Baby Sling</div>
    </div>

    <p class="tagline">Premium, high-quality, natural, appeal to parents of new baby, gender-neutral, modern and funky.</p>

    <div class="brand">Cradle<br>Bloom</div>
  </main>
</body>
</html>
```